Vextara website

Web design for small consulting firm
It can be simple, easy to find approach

The primary use is business to business for

a. people wanting to find out a bit more of us after receiving a business card
b. Search words to draw people from search engines to us

Target Market(s)

Senior staff of large companies, in their work capacity
MD / CEO / CFO , directors, etc.

Industry/Entity Type

Business

Colors
ffffff
f79020
faa54b
33a6d7

```html
<!DOCTYPE html>
<html lang="en">
<head>
<meta charset="utf-8">
<title>Vextara – Consulting</title>
<link href="https://fonts.googleapis.com/css2?family=Open+Sans:wght@400;600;700;800&display=swap" rel="stylesheet">
<style>
:root{
  --white:#ffffff;
  --orange:#f79020;
  --orange-light:#faa54b;
  --blue:#33a6d7;
  --ink:#2f2f2f;
  --grey-text:#666;
  --grey-light:#eeeeee;
  --grey-btn:#5b5b5b;
  --footer:#3d3d3d;
}
*{margin:0;padding:0;box-sizing:border-box}
html,body{width:845px;height:1200px;overflow:hidden}
body{font-family:"Open Sans",Arial,sans-serif;color:var(--ink);background:var(--white);position:relative}
.header{height:80px;position:relative;background:var(--white)}
.brand{position:absolute;left:40px;top:18px;display:flex;align-items:center;gap:8px}
.brand-dot{width:14px;height:14px;border-radius:50%;background:var(--blue)}
.brand-name{font-size:26px;font-weight:700;color:var(--blue);letter-spacing:-0.5px}
.contact{position:absolute;right:40px;top:12px;display:flex;gap:16px;font-size:9px;color:var(--grey-text);align-items:center}
.contact span{display:flex;align-items:center;gap:4px}
.contact svg{width:10px;height:10px}
.nav{position:absolute;right:40px;top:44px;display:flex;gap:30px;font-size:10px;color:var(--grey-text)}
.nav a{color:inherit;text-decoration:none}
.nav a.active{color:var(--orange)}
.hero{height:200px;position:relative;background:linear-gradient(180deg,#f7f7f7,#e3e3e3);overflow:hidden}
.hero-copy{position:absolute;left:110px;top:22px;width:320px}
.hero-kicker{font-size:32px;font-weight:800;color:var(--orange);line-height:1}
.hero-title{font-size:32px;font-weight:800;color:var(--ink);line-height:1.1}
.hero-rule{width:220px;height:2px;background:var(--blue);margin:6px 0 8px}
.hero-lead{font-size:11px;line-height:1.4;color:#444}
.hero-sub{font-size:7px;line-height:1.5;color:var(--grey-text);margin-top:6px}
.btn{display:inline-block;background:var(--grey-btn);color:var(--white);font-size:8px;font-weight:700;padding:7px 18px;border-radius:3px;text-transform:uppercase;margin-top:10px}
.hero-visual{position:absolute;right:110px;top:10px;width:230px;height:185px;border-radius:50%;background:radial-gradient(circle,#f3c35a,#c98a1c 60%,#e3e3e3 72%)}
.arrow{position:absolute;top:88px;width:20px;height:20px;border-radius:50%;background:rgba(0,0,0,.15)}
.arrow.left{left:16px}.arrow.right{right:16px}
.arrow svg{width:20px;height:20px}
.talk{height:480px;background:var(--orange);text-align:center;color:var(--white);position:relative}
.talk h2{font-size:22px;font-weight:700;padding-top:24px;letter-spacing:.5px}
.section-text{font-size:7.5px;line-height:1.6;width:460px;margin:8px auto 0;color:#fff6ea}
.cards{display:flex;gap:8px;justify-content:center;margin-top:24px}
.card{width:120px;height:150px;background:var(--white);border-radius:3px;overflow:hidden;color:var(--grey-text)}
.card-img{height:72px}
.card h3{font-size:7px;color:var(--orange);font-weight:700;margin:5px 0 3px}
.card p{font-size:6px;line-height:1.5;padding:0 8px}
.who{margin-top:22px}
.talk .btn{margin-top:14px;padding:8px 24px}
.clients{height:210px;text-align:center;position:relative}
.clients h2{font-size:13px;font-weight:700;color:var(--orange);padding-top:28px}
.quote{font-size:9px;color:var(--grey-text);margin-top:14px}
.quote-small{font-size:7px;line-height:1.6;color:#888;width:420px;margin:8px auto 0}
.dots{display:flex;gap:6px;justify-content:center;margin-top:18px}
.dots i{width:7px;height:7px;border-radius:50%;background:#ccc}
.dots i.on{background:var(--orange)}
.partners{height:100px;background:var(--grey-light);display:flex;justify-content:center;align-items:center;gap:58px}
.partner{display:flex;align-items:center;gap:6px;font-size:15px;font-weight:600;color:#555}
.partner b{width:12px;height:12px;border-radius:50%;background:#555;display:block}
.footer{position:absolute;left:0;bottom:0;width:845px;height:130px;background:var(--footer);color:#bbb}
.footer-brand{position:absolute;left:120px;top:26px;font-size:20px;font-weight:700;color:#ddd}
.footer-nav{position:absolute;left:260px;top:34px;display:flex;gap:26px;font-size:8px}
.footer-copy{position:absolute;left:120px;top:58px;font-size:7px;color:#999}
</style>
</head>
<body>
<header class="header">
  <div class="brand"><span class="brand-dot"></span><span class="brand-name">Vextara</span></div>
  <div class="contact">
    <span><svg viewBox="0 0 10 10"><path d="M2 1l2 2-1 1a5 5 0 0 0 3 3l1-1 2 2-1 1C4 9 1 6 1 2z" fill="#888"/></svg>021 555 0142</span>
    <span><svg viewBox="0 0 10 10"><rect x="1" y="2" width="8" height="6" fill="none" stroke="#888"/><path d="M1 2l4 3 4-3" fill="none" stroke="#888"/></svg>hello@vextara.example</span>
  </div>
  <nav class="nav">
    <a class="active" href="#">Home</a><a href="#">Our values</a><a href="#">What we do</a><a href="#">Articles and publications</a><a href="#">Useful links</a>
  </nav>
</header>

<section class="hero">
  <span class="arrow left"><svg viewBox="0 0 20 20"><path d="M12 5l-5 5 5 5" fill="none" stroke="#fff" stroke-width="2"/></svg></span>
  <div class="hero-copy">
    <div class="hero-kicker">WE ARE A</div>
    <div class="hero-title">CONSULTING FIRM</div>
    <div class="hero-rule"></div>
    <p class="hero-lead">The primary focus is to assist companies in their quest to enhance performance</p>
    <p class="hero-sub">Our focus is on stewardship, helping senior leaders and directors steer their firms toward clear goals and lasting value. That is what stewardship is all about.</p>
    <span class="btn">Read more</span>
  </div>
  <div class="hero-visual" role="img" aria-label="Golden figure holding up a glowing light bulb"></div>
  <span class="arrow right"><svg viewBox="0 0 20 20"><path d="M8 5l5 5-5 5" fill="none" stroke="#fff" stroke-width="2"/></svg></span>
</section>

<section class="talk">
  <h2>TALK TO US ABOUT</h2>
  <p class="section-text">The primary focus is to assist companies in their quest to enhance performance. Our focus is on stewardship, making sure directors and senior managers are placed in a position of trust to manage resources wisely. That is what stewardship is all about.</p>
  <div class="cards">
    <div class="card"><div class="card-img" role="img" aria-label="Business people shaking hands" style="background:linear-gradient(#9fb3c4,#d9dfe5)"></div><h3>Governance</h3><p>Clear boards, sound policy and steady oversight for growing firms.</p></div>
    <div class="card"><div class="card-img" role="img" aria-label="Hands holding a young green plant" style="background:linear-gradient(#8cbf6a,#e2efd7)"></div><h3>Stewardship</h3><p>Guiding leaders to manage resources with trust and care.</p></div>
    <div class="card"><div class="card-img" role="img" aria-label="Hands stacked together in teamwork" style="background:linear-gradient(#d9a98a,#f1dfd3)"></div><h3>Performance</h3><p>Practical steps that lift results across the whole business.</p></div>
    <div class="card"><div class="card-img" role="img" aria-label="Office workers planning around a desk" style="background:linear-gradient(#7fa7c9,#dce7f0)"></div><h3>Strategy</h3><p>Focused plans that help directors set clear long term goals.</p></div>
  </div>
  <h2 class="who">WHO WE ARE</h2>
  <p class="section-text">The primary focus is to assist companies in their quest to enhance performance. Our focus is on stewardship, making sure directors and senior managers are placed in a position of trust to manage resources wisely. That is what stewardship is all about.</p>
  <span class="btn">Click here</span>
</section>

<section class="clients">
  <h2>WHAT CLIENTS SAY</h2>
  <p class="quote">Vextara helped our board find clear focus and a steadier way forward.</p>
  <p class="quote-small">Their team listened carefully, asked the right questions and gave us practical advice that our directors could act on at once. We would gladly work with them again.</p>
  <div class="dots"><i class="on"></i><i></i><i></i></div>
</section>

<section class="partners">
  <span class="partner"><b></b>Lumora</span>
  <span class="partner">Brightfield</span>
  <span class="partner"><b></b>Castelo</span>
  <span class="partner">Norvale</span>
  <span class="partner">Quilby</span>
</section>

<footer class="footer">
  <div class="footer-brand">Vextara</div>
  <div class="footer-nav"><span>Home</span><span>Our values</span><span>What we do</span><span>Articles and publications</span><span>Useful links</span></div>
  <div class="footer-copy">© 2024 Vextara. All rights reserved.</div>
</footer>
</body>
</html>
```